Real Estate Listing Landing Page

I am looking for a landing page for my Flat Fee MLS Listing website... The name of my website is "Keybright Home Deals".

I am a big fan of this landing page setup and would like something similar.
https://sellbrightpath.com/

I am a fan of the design style on https://sellbrightpath.com/ and also this design style as well... https://2417.gleamhorizon.com/

Use your creativity and incorporate your own twists that you would feel lift up this landing pages' appeal. I'd love some red color incorporated within the design.

Target Market(s)

Real Estate Home Sellers

Industry/Entity Type

Real Estate

Coding

Coded - Design and coding required

Font styles to use
Sans Serif

Colors
0054AA
0677BA
7BADD7
CADEEF
E8F1F8
0094D4
00A9DD
6FCCEA
C7EBF8
E9F6FB
EB3D1F
EC4F4E
F09395
F8D3D4
FCEDEE

```html
<!DOCTYPE html>
<html lang="en">
<head>
<meta charset="utf-8">
<title>Keybright Home Deals – Flat Fee MLS Listing</title>
<link href="https://fonts.googleapis.com/css2?family=Bebas+Neue&family=Roboto:ital,wght@0,400;0,500;0,700;1,400&family=Poppins:wght@400;600&display=swap" rel="stylesheet">
<style>
:root{
  --red:#EB3D1F;
  --red-soft:#EC4F4E;
  --red-pale:#F8D3D4;
  --red-faint:#FCEDEE;
  --ink:#1d1d1d;
  --text:#333;
  --muted:#8a8a8a;
  --line:#e4e4e4;
  --bg-soft:#f6f6f6;
  --footer:#2b0b0b;
  --white:#fff;
}
*{margin:0;padding:0;box-sizing:border-box}
html,body{width:1200px;height:3897px;overflow:hidden}
body{font-family:'Roboto',sans-serif;color:var(--text);background:var(--white);position:relative}
.abs{position:absolute}
.display{font-family:'Bebas Neue',sans-serif;font-weight:400;color:var(--ink);letter-spacing:.5px}
.accent{color:var(--red)}
.btn{position:absolute;background:var(--red);color:#fff;font-family:'Bebas Neue',sans-serif;letter-spacing:1.5px;font-size:13px;display:flex;align-items:center;justify-content:center;box-shadow:0 6px 14px rgba(235,61,31,.3)}

/* top bar */
.topbar{position:absolute;left:0;top:0;width:1200px;height:37px;background:var(--red);color:#fff;font-size:13px}
.topbar .social{position:absolute;left:101px;top:11px;display:flex;gap:7px}
.topbar .social span{width:14px;height:14px;border:1.5px solid #fff;border-radius:50%}
.topbar .links{position:absolute;left:590px;top:0;height:37px;display:flex;align-items:center}
.topbar .links a{color:#fff;text-decoration:none;padding:0 34px;border-right:1px solid rgba(255,255,255,.7);line-height:16px}
.topbar .links a:first-child{padding-left:20px}
.topbar .cart{position:absolute;left:1066px;top:9px}

/* nav */
.nav{position:absolute;left:0;top:37px;width:1200px;height:75px;background:#fff}
.logo{position:absolute;font-family:'Roboto',sans-serif;font-weight:700;color:var(--red);display:flex;align-items:center;gap:7px}
.logo i{display:block;width:12px;height:12px;background:var(--red)}
.nav .logo{left:101px;top:27px;font-size:17px}
.menu{position:absolute;left:408px;top:0;height:75px;display:flex;font-size:13px}
.menu a{color:var(--ink);text-decoration:none;height:75px;display:flex;align-items:center;padding:0 16px}
.menu a.active{background:#f1f1f1;color:var(--red);padding:0 12px;width:58px;justify-content:center}
.nav .btn{left:967px;top:17px;width:130px;height:40px}

/* hero */
.hero{position:absolute;left:0;top:112px;width:1200px;height:531px}
.hero .photo{position:absolute;inset:0;background:linear-gradient(180deg,#dfe7ea 0%,#eef1f2 45%,#cfd8da 62%,#6fa6ad 80%,#3f8793 100%)}
.hero h1{position:absolute;left:101px;top:150px;font-size:46px;line-height:48px}
.hero p{position:absolute;left:101px;top:270px;width:420px;font-size:13px;line-height:20px;color:#222}
.hero .btn{top:342px;height:40px}
.arrow{position:absolute;top:255px}

/* section titles */
.sec-title{position:absolute;left:0;width:1200px;text-align:center;font-size:44px;line-height:48px}
.sec-sub{position:absolute;left:0;width:1200px;text-align:center;font-size:13px;line-height:21px;color:#222}

/* pricing */
.plan{position:absolute;top:864px;width:268px;height:424px;background:#fff;border:1px solid #ececec;text-align:center}
.plan h3{margin-top:30px;font-size:13px;font-weight:700;color:var(--ink)}
.plan .price{margin-top:10px;font-family:'Bebas Neue',sans-serif;font-size:36px;color:var(--red);line-height:36px}
.plan .price sup{font-family:'Roboto',sans-serif;font-size:11px;vertical-align:16px;margin-right:2px}
.plan .period{margin-top:6px;font-size:13px;color:var(--muted)}
.plan .for{margin-top:14px;font-size:13px;color:#222;padding-bottom:22px;border-bottom:1px solid var(--line);margin-left:28px;margin-right:28px}
.plan ul{list-style:none;margin:22px auto 0;width:130px;text-align:left}
.plan li{font-size:13px;color:#222;height:28px;display:flex;align-items:center;gap:9px}
.plan .rule{margin:14px 28px 0;border-top:1px solid var(--line)}
.plan .btn{position:relative;margin:20px auto 0;width:86px;height:32px;font-size:12px}

/* sold */
.sold-band{position:absolute;left:0;top:1347px;width:1200px;height:375px;background:linear-gradient(90deg,#d8391f,#ec4f3e 50%,#d8391f)}
.sold-title{position:absolute;left:0;top:1405px;width:1200px;text-align:center;color:#fff;font-size:46px;line-height:48px}
.sold-card{position:absolute;top:1559px;width:302px;height:362px;background:#fff;box-shadow:0 8px 22px rgba(0,0,0,.1)}
.sold-card .img{position:absolute;left:15px;top:15px;width:272px;height:229px}
.sold-card .for{position:absolute;left:16px;top:260px;font-size:12px;font-style:italic;font-weight:500;color:#222}
.sold-card .saved{position:absolute;left:16px;top:280px;font-family:'Bebas Neue',sans-serif;font-size:28px;color:var(--red)}
.sold-card .saved small{font-size:12px;color:var(--ink)}
.sold-card .addr{position:absolute;left:16px;top:318px;font-size:8.5px;font-style:italic;color:#999}
.sold-card .date{position:absolute;left:16px;top:335px;font-size:7.5px;font-style:italic;color:#bbb}
.circle-arrow{position:absolute;top:1700px;width:46px;height:46px;border-radius:50%;background:#fff;box-shadow:0 3px 12px rgba(0,0,0,.15);display:flex;align-items:center;justify-content:center}

/* how it works */
.step{position:absolute;top:2150px;width:240px;text-align:center}
.step .diamond{position:relative;margin:0 auto;width:200px;height:200px}
.step .frame{position:absolute;left:34px;top:34px;width:132px;height:132px;border:2px solid var(--red);transform:rotate(45deg)}
.step .fill{position:absolute;left:45px;top:45px;width:110px;height:110px;transform:rotate(45deg)}
.step h4{margin-top:26px;font-family:'Bebas Neue',sans-serif;font-weight:400;font-size:21px;color:var(--ink);letter-spacing:.3px}

/* testimonials */
.testi-bg{position:absolute;left:0;top:2572px;width:1200px;height:466px;background:var(--bg-soft)}
.quote{position:absolute;top:2723px;width:391px;height:167px;background:#fff}
.quote p{position:absolute;left:30px;top:30px;width:331px;text-align:center;font-size:12px;line-height:21px;font-style:italic;color:#444}
.quote .stars{position:absolute;left:0;top:126px;width:391px;text-align:center;color:var(--red);font-size:17px;letter-spacing:4px}
.quote .q{position:absolute;font-family:Georgia,serif;font-size:90px;color:var(--red-pale);line-height:1}
.author{position:absolute;top:2898px;display:flex;align-items:center;gap:14px}
.author .av{width:38px;height:38px;border-radius:50%;background:linear-gradient(135deg,#d9d2e4,#a99bc2)}
.author b{display:block;font-family:'Poppins',sans-serif;font-size:13px;color:var(--red);font-weight:600}
.author span{font-size:11px;color:#555}
.dots{position:absolute;left:576px;top:2992px;display:flex;gap:5px;align-items:center}
.dots i{width:3px;height:3px;border-radius:50%;background:#c9c9c9}
.dots i.on{width:5px;height:5px;background:var(--red)}

/* service areas */
.areas-label{position:absolute;left:0;top:3038px;width:101px;height:465px;background:var(--red)}
.areas-label span{position:absolute;left:50%;top:50%;transform:translate(-50%,-50%) rotate(-90deg);font-family:'Bebas Neue',sans-serif;font-size:44px;color:#fff;white-space:nowrap;letter-spacing:1px}
.map{position:absolute;left:101px;top:3038px;width:1099px;height:465px;background:linear-gradient(135deg,#a7d3a0 0%,#d9e6bf 35%,#eee9cf 55%,#c2deaa 80%,#9fcfe0 100%)}

/* footer */
.footer{position:absolute;left:0;top:3503px;width:1200px;height:394px;background:var(--footer);color:#e8dede}
.footer .logo{left:101px;top:88px;font-size:22px;color:#fff}
.footer .logo i{background:#fff}
.footer .about{position:absolute;left:101px;top:178px;font-size:13px;line-height:21px;width:270px;color:#e2d6d6}
.fcol{position:absolute;top:92px}
.fcol h5{font-family:'Bebas Neue',sans-serif;font-weight:400;font-size:15px;letter-spacing:1.2px;color:#fff;margin-bottom:18px}
.fcol a{display:block;font-size:13px;color:#e2d6d6;text-decoration:none;line-height:24px}
.fcol .row{display:flex;align-items:center;gap:16px;font-size:13px;line-height:34px}
.fcol .follow{margin-top:10px;font-family:'Bebas Neue',sans-serif;font-size:15px;letter-spacing:1px;display:flex;align-items:center;gap:6px;color:#fff}
.fcol .follow i{width:14px;height:14px;border:1.5px solid #fff;border-radius:50%}
.footer .rule{position:absolute;left:101px;top:313px;width:996px;border-top:1px solid rgba(255,255,255,.3)}
.footer .copy{position:absolute;left:101px;top:342px;font-size:13px}
.footer .legal{position:absolute;right:103px;top:342px;font-size:13px}
</style>
</head>
<body>

<header class="topbar">
  <div class="social"><span></span><span></span><span></span></div>
  <nav class="links"><a href="#">Help center</a><a href="#">Listing dashboard</a><a href="#">Login/register</a></nav>
  <svg class="cart" width="20" height="18" viewBox="0 0 20 18" fill="none" stroke="#fff" stroke-width="1.6"><path d="M1 2h3l2 10h10l2-7H5"/><circle cx="8" cy="15.5" r="1.3"/><circle cx="15" cy="15.5" r="1.3"/></svg>
</header>

<div class="nav">
  <div class="logo"><i></i>Keybright Home Deals</div>
  <nav class="menu"><a class="active" href="#">Home</a><a href="#">About uS</a><a href="#">Pricing</a><a href="#">Contact Us</a><a href="#">News</a></nav>
  <a class="btn" href="#">List your home</a>
</div>

<section class="hero">
  <div class="photo" role="img" aria-label="Photo of a white modern house with a turquoise pool"></div>
  <h1 class="display"><span class="accent">Selling your home</span> with us<br>will save you thousands.</h1>
  <p>Lorem Ipsum is simply dummy text of the printing and typesetting industry. Lorem IpsumLorem Ipsum is simply</p>
  <a class="btn" href="#" style="left:101px;width:130px">List your home</a>
  <a class="btn" href="#" style="left:245px;width:109px">Learn more</a>
  <svg class="arrow" style="left:35px" width="12" height="16" viewBox="0 0 12 16" fill="none" stroke="#111" stroke-width="2"><path d="M9 2 3 8l6 6"/></svg>
  <svg class="arrow" style="left:1153px" width="12" height="16" viewBox="0 0 12 16" fill="none" stroke="#111" stroke-width="2"><path d="m3 2 6 6-6 6"/></svg>
</section>

<h2 class="display sec-title" style="top:702px">Our flexible <span class="accent">pricing</span></h2>
<p class="sec-sub" style="top:774px">Lorem ipsum dolor sit amet, consetetur sadipscing<br>elitr, sed diam nonumy</p>

<div class="plan" style="left:171px">
  <h3>Silver Plan</h3><div class="price"><sup>$</sup>149</div><div class="period">Every 6 month</div><div class="for">Perfect for home owners</div>
  <ul>
    <li><svg width="15" height="15" viewBox="0 0 15 15" fill="none" stroke="#EB3D1F" stroke-width="1.4"><circle cx="7.5" cy="7.5" r="6.5"/><path d="m4.5 7.6 2 2 4-4"/></svg>Plan feature 01</li>
    <li><svg width="15" height="15" viewBox="0 0 15 15" fill="none" stroke="#EB3D1F" stroke-width="1.4"><circle cx="7.5" cy="7.5" r="6.5"/><path d="m4.5 7.6 2 2 4-4"/></svg>Plan feature 01</li>
    <li><svg width="15" height="15" viewBox="0 0 15 15" fill="none" stroke="#EB3D1F" stroke-width="1.4"><circle cx="7.5" cy="7.5" r="6.5"/><path d="m4.5 7.6 2 2 4-4"/></svg>Plan feature 01</li>
    <li><svg width="15" height="15" viewBox="0 0 15 15" fill="none" stroke="#EB3D1F" stroke-width="1.4"><circle cx="7.5" cy="7.5" r="6.5"/><path d="m4.5 7.6 2 2 4-4"/></svg>Plan feature 01</li>
    <li><svg width="15" height="15" viewBox="0 0 15 15" fill="none" stroke="#EB3D1F" stroke-width="1.4"><circle cx="7.5" cy="7.5" r="6.5"/><path d="m4.5 7.6 2 2 4-4"/></svg>Plan feature 01</li>
  </ul>
  <div class="rule"></div><a class="btn" href="#">List now</a>
</div>
<div class="plan" style="left:467px">
  <h3>Silver Plan</h3><div class="price"><sup>$</sup>149</div><div class="period">Every 6 month</div><div class="for">Perfect for home owners</div>
  <ul>
    <li><svg width="15" height="15" viewBox="0 0 15 15" fill="none" stroke="#EB3D1F" stroke-width="1.4"><circle cx="7.5" cy="7.5" r="6.5"/><path d="m4.5 7.6 2 2 4-4"/></svg>Plan feature 01</li>
    <li><svg width="15" height="15" viewBox="0 0 15 15" fill="none" stroke="#EB3D1F" stroke-width="1.4"><circle cx="7.5" cy="7.5" r="6.5"/><path d="m4.5 7.6 2 2 4-4"/></svg>Plan feature 01</li>
    <li><svg width="15" height="15" viewBox="0 0 15 15" fill="none" stroke="#EB3D1F" stroke-width="1.4"><circle cx="7.5" cy="7.5" r="6.5"/><path d="m4.5 7.6 2 2 4-4"/></svg>Plan feature 01</li>
    <li><svg width="15" height="15" viewBox="0 0 15 15" fill="none" stroke="#EB3D1F" stroke-width="1.4"><circle cx="7.5" cy="7.5" r="6.5"/><path d="m4.5 7.6 2 2 4-4"/></svg>Plan feature 01</li>
    <li><svg width="15" height="15" viewBox="0 0 15 15" fill="none" stroke="#EB3D1F" stroke-width="1.4"><circle cx="7.5" cy="7.5" r="6.5"/><path d="m4.5 7.6 2 2 4-4"/></svg>Plan feature 01</li>
  </ul>
  <div class="rule"></div><a class="btn" href="#">List now</a>
</div>
<div class="plan" style="left:762px">
  <h3>Silver Plan</h3><div class="price"><sup>$</sup>149</div><div class="period">Every 6 month</div><div class="for">Perfect for home owners</div>
  <ul>
    <li><svg width="15" height="15" viewBox="0 0 15 15" fill="none" stroke="#EB3D1F" stroke-width="1.4"><circle cx="7.5" cy="7.5" r="6.5"/><path d="m4.5 7.6 2 2 4-4"/></svg>Plan feature 01</li>
    <li><svg width="15" height="15" viewBox="0 0 15 15" fill="none" stroke="#EB3D1F" stroke-width="1.4"><circle cx="7.5" cy="7.5" r="6.5"/><path d="m4.5 7.6 2 2 4-4"/></svg>Plan feature 01</li>
    <li><svg width="15" height="15" viewBox="0 0 15 15" fill="none" stroke="#EB3D1F" stroke-width="1.4"><circle cx="7.5" cy="7.5" r="6.5"/><path d="m4.5 7.6 2 2 4-4"/></svg>Plan feature 01</li>
    <li><svg width="15" height="15" viewBox="0 0 15 15" fill="none" stroke="#EB3D1F" stroke-width="1.4"><circle cx="7.5" cy="7.5" r="6.5"/><path d="m4.5 7.6 2 2 4-4"/></svg>Plan feature 01</li>
    <li><svg width="15" height="15" viewBox="0 0 15 15" fill="none" stroke="#EB3D1F" stroke-width="1.4"><circle cx="7.5" cy="7.5" r="6.5"/><path d="m4.5 7.6 2 2 4-4"/></svg>Plan feature 01</li>
  </ul>
  <div class="rule"></div><a class="btn" href="#">List now</a>
</div>

<div class="sold-band" role="img" aria-label="Red-tinted photo of a living room interior"></div>
<h2 class="display sold-title">See how our customers saved<br>recently sold properties</h2>

<article class="sold-card" style="left:126px">
  <div class="img" role="img" aria-label="Photo of a white cottage house with autumn trees" style="background:linear-gradient(160deg,#e9d7b9,#c8a56a 40%,#8f9a5a 80%,#6c7d3f)"></div>
  <div class="for">Sold for: $180,000.00</div>
  <div class="saved">$18,000.00 <small>commission saved !</small></div>
  <div class="addr">482 Linden Court East Riverton, SC 29811</div>
  <div class="date">Sold At : 22 Jan 2023</div>
</article>
<article class="sold-card" style="left:449px">
  <div class="img" role="img" aria-label="Photo of a modern white villa with a pool" style="background:linear-gradient(170deg,#8fc3ea,#dfe8ee 45%,#b9c2c6 70%,#4f7d5a)"></div>
  <div class="for">Sold for: $180,000.00</div>
  <div class="saved">$18,000.00 <small>commission saved !</small></div>
  <div class="addr">482 Linden Court East Riverton, SC 29811</div>
  <div class="date">Sold At : 22 Jan 2023</div>
</article>
<article class="sold-card" style="left:772px">
  <div class="img" role="img" aria-label="Photo of a large grey family house with a lawn" style="background:linear-gradient(175deg,#bcd8ef,#e6eef4 35%,#8b93a0 60%,#5f9e3c 85%)"></div>
  <div class="for">Sold for: $180,000.00</div>
  <div class="saved">$18,000.00 <small>commission saved !</small></div>
  <div class="addr">482 Linden Court East Riverton, SC 29811</div>
  <div class="date">Sold At : 22 Jan 2023</div>
</article>
<div class="circle-arrow" style="left:101px"><svg width="10" height="14" viewBox="0 0 10 14" fill="none" stroke="#EB3D1F" stroke-width="2"><path d="M7 2 2 7l5 5"/></svg></div>
<div class="circle-arrow" style="left:1050px"><svg width="10" height="14" viewBox="0 0 10 14" fill="none" stroke="#EB3D1F" stroke-width="2"><path d="m3 2 5 5-5 5"/></svg></div>

<h2 class="display sec-title" style="top:1988px">How it <span class="accent">works</span></h2>
<p class="sec-sub" style="top:2059px">Lorem ipsum dolor sit amet, consetetur sadipscing<br>elitr, sed diam nonumy</p>

<div class="step" style="left:77px"><div class="diamond"><div class="frame"></div><div class="fill" role="img" aria-label="Photo of a hand choosing a package on paperwork" style="background:linear-gradient(135deg,#f39a3a,#e3e3e8 60%,#7a6a64)"></div></div><h4>Choose your package</h4></div>
<div class="step" style="left:344px"><div class="diamond"><div class="frame"></div><div class="fill" role="img" aria-label="Photo of a modern house facade at dusk" style="background:linear-gradient(135deg,#5a5f8c,#b07b6a 55%,#6b4a3f)"></div></div><h4>Complete online listing forms</h4></div>
<div class="step" style="left:620px"><div class="diamond"><div class="frame"></div><div class="fill" role="img" aria-label="Photo of a bright living room with a patterned rug" style="background:linear-gradient(135deg,#f2f2f0,#c9ccc9 50%,#8a3f2e)"></div></div><h4>We list you on the local MLS</h4></div>
<div class="step" style="left:880px"><div class="diamond"><div class="frame"></div><div class="fill" role="img" aria-label="Photo of a cosy grey sofa in a living room" style="background:linear-gradient(135deg,#e8e8e6,#b2b1ad 55%,#7d7a74)"></div></div><h4>You save thousands</h4></div>
<a class="btn" href="#" style="left:535px;top:2459px;width:129px;height:39px">List your home</a>

<div class="testi-bg"></div>
<h2 class="display sec-title" style="top:2628px">What our client say</h2>

<div class="quote" style="left:101px"><span class="q" style="left:26px;top:108px">&ldquo;</span><span class="q" style="left:306px;top:6px">&rdquo;</span><p>Lorem Ipsum is simply dummy text of the printing and typesetting industry. Lorem IpsumLorem Ipsum is simply dummy text of the printing and typesetting industry. Lorem Ipsum</p><div class="stars">★★★★★</div></div>
<div class="quote" style="left:514px"><span class="q" style="left:26px;top:108px">&ldquo;</span><span class="q" style="left:306px;top:6px">&rdquo;</span><p>Lorem Ipsum is simply dummy text of the printing and typesetting industry. Lorem IpsumLorem Ipsum is simply dummy text of the printing and typesetting industry. Lorem Ipsum</p><div class="stars">★★★★★</div></div>
<div class="quote" style="left:924px"><span class="q" style="left:26px;top:108px">&ldquo;</span><span class="q" style="left:306px;top:6px">&rdquo;</span><p>Lorem Ipsum is simply dummy text of the printing and typesetting industry. Lorem IpsumLorem Ipsum is simply dummy text of the printing and typesetting industry. Lorem Ipsum</p><div class="stars">★★★★★</div></div>

<div class="author" style="left:101px"><div class="av" role="img" aria-label="Client portrait"></div><div><b>Dana M</b><span>Home Owner</span></div></div>
<div class="author" style="left:514px"><div class="av" role="img" aria-label="Client portrait"></div><div><b>Dana M</b><span>Home Owner</span></div></div>
<div class="author" style="left:924px"><div class="av" role="img" aria-label="Client portrait"></div><div><b>Dana M</b><span>Home Owner</span></div></div>
<div class="dots"><i></i><i></i><i class="on"></i><i></i><i></i></div>

<div class="areas-label"><span>Service areas</span></div>
<div class="map" role="img" aria-label="Map of the United States with red pins marking service cities"></div>

<footer class="footer">
  <div class="logo"><i></i>Keybright Home Deals</div>
  <p class="about">Lorem Ipsum Dolor Sit Amet, Consetetur Sadipscing Elitr, Sed Diam Nonumy Eirmod Tempor Invidunt Ut Labore Et</p>
  <div class="fcol" style="left:475px"><h5>Quick links</h5><a href="#">Home</a><a href="#">About Us</a><a href="#">Pricing</a><a href="#">Testimonials</a><a href="#">Blog</a><a href="#">Contact us</a></div>
  <div class="fcol" style="left:682px"><h5>Services areas</h5><a href="#">Service Area 01</a><a href="#">Service Area 02</a><a href="#">Service Area 03</a><a href="#">Service Area 04</a><a href="#">Service Area 05</a><a href="#">Service Area 06</a></div>
  <div class="fcol" style="left:868px"><h5>Get in touch</h5>
    <div class="row"><svg width="16" height="16" viewBox="0 0 16 16" fill="#fff"><path d="M3.5 1.5 6 4 4.8 6.2c.9 2 2.5 3.6 4.5 4.5L11.5 9.5 14 12l-1.8 2.3C6.6 13.8 2.2 9.4 1.7 3.8z"/></svg>1-555-204-7716</div>
    <div class="row"><svg width="16" height="16" viewBox="0 0 16 16" fill="none" stroke="#fff" stroke-width="1.4"><rect x="1.5" y="3.5" width="13" height="9" rx="1"/><path d="m2 4 6 5 6-5"/></svg>hello@keybrighthomedeals.com</div>
    <div class="row"><svg width="16" height="16" viewBox="0 0 16 16" fill="none" stroke="#fff" stroke-width="1.4"><path d="M8 15s5-5 5-8.5A5 5 0 0 0 3 6.5C3 10 8 15 8 15z"/><circle cx="8" cy="6.5" r="1.8"/></svg>Unites States North America</div>
    <div class="follow">Follow us : <i></i><i></i><i></i></div>
  </div>
  <div class="rule"></div>
  <div class="copy">© 2023 Keybright Home Deals All rights reserved</div>
  <div class="legal">Site map &nbsp;|&nbsp; Terms and conditions &nbsp;|&nbsp; Privacy Policy</div>
</footer>

</body>
</html>
```